Business Cards Needed for Innovative Healthcare Marketing Company

We are a marketing company focused on healthcare. Our company is all about rebranding yourself renewing your image and generating results. The phoenix stands for "reborn" or "rising" which we provide new brands for our clients we take their old brands and renew it with creativity and innovation. I am looking for a business card with color dimension. I have attached an example of a card I think has the look and feel of what I am trying to accomplish. I like that the card example has black and grey font colors, I like the font placement and the small logo, I really like the use of the colors on the right those are the colors of my logo. My logo is phoenix so maybe incorporating flames similar to that design. I would like the back a solid color maybe red with an opaque version of the logo and website. As a marketing company I am always open to creative liberty!

Target Market(s)

Doctors and business professionals.

Industry/Entity Type

Marketing

Contact Information for Business Card

Vornaly Health Care Marketing
Marnie Okonski- CEO
#(502)638-2947
email-marnie@vornaly.com
website- vornaly.com

Font styles to use
Sans Serif

Colors
ec1f27
f37122
ffc214
fbed22
fbf289
f04a50

Requirements
Must have
• The logo and required information
Nice to have
• icons by the information
Should not have
• child like font

```html
<!DOCTYPE html>
<html lang="en">
<head>
<meta charset="utf-8">
<title>Vornaly Health Care Marketing – Business Card</title>
<link rel="stylesheet" href="https://fonts.googleapis.com/css2?family=Quicksand:wght@400;500;600;700&display=swap">
<style>
  :root {
    --page-bg: #dedad7;
    --card-top: #f4f1ef;
    --card-top-shade: #e7e2df;
    --band-light: #8e1c20;
    --band-dark: #5a0e12;
    --accent-orange: #f37122;
    --accent-line: #e0662a;
    --logo-red: #7c1c22;
    --band-text: #f1e3e1;
    --role-text: #d9c6c4;
  }
  * { margin: 0; padding: 0; box-sizing: border-box; }
  html, body {
    width: 1200px;
    height: 969px;
    overflow: hidden;
    background: var(--page-bg);
    font-family: "Quicksand", sans-serif;
  }
  .business-card {
    position: absolute;
    left: 100px;
    top: 200px;
    width: 1000px;
    height: 570px;
    border-radius: 22px;
    overflow: hidden;
    background: linear-gradient(160deg, var(--card-top) 0%, var(--card-top-shade) 100%);
    box-shadow: 0 14px 40px rgba(60, 30, 30, 0.18);
  }
  .card-band {
    position: absolute;
    left: 0;
    top: 0;
    width: 1000px;
    height: 570px;
  }
  .brand-mark {
    position: absolute;
    left: 250px;
    top: 120px;
    width: 140px;
    height: 140px;
    border-radius: 50%;
    background: var(--accent-orange);
  }
  .brand-name {
    position: absolute;
    left: 440px;
    top: 150px;
    color: var(--logo-red);
    font-weight: 500;
  }
  .brand-name .brand-word {
    display: block;
    font-size: 68px;
    line-height: 1;
    letter-spacing: 2px;
  }
  .brand-name .brand-rule {
    display: block;
    height: 2px;
    width: 328px;
    margin: 14px 0 6px;
    background: var(--logo-red);
  }
  .brand-name .brand-tagline {
    display: block;
    font-size: 22px;
    letter-spacing: 1.5px;
  }
  .card-holder {
    position: absolute;
    right: 558px;
    top: 410px;
    text-align: right;
  }
  .holder-name {
    color: var(--accent-orange);
    font-weight: 700;
    font-size: 34px;
    letter-spacing: 1px;
  }
  .holder-role {
    color: var(--role-text);
    font-size: 24px;
    font-weight: 500;
    margin-top: 4px;
    letter-spacing: 1px;
  }
  .contact-list {
    position: absolute;
    left: 490px;
    top: 402px;
    list-style: none;
  }
  .contact-item {
    display: flex;
    align-items: center;
    height: 38px;
    color: var(--band-text);
    font-size: 26px;
    font-weight: 500;
    letter-spacing: 1px;
  }
  .contact-icon {
    width: 22px;
    height: 22px;
    margin-right: 18px;
    fill: var(--accent-orange);
    flex-shrink: 0;
  }
</style>
</head>
<body>
  <div class="business-card">
    <svg class="card-band" viewBox="0 0 1000 570" aria-hidden="true">
      <defs>
        <linearGradient id="bandFill" x1="0" y1="0" x2="1" y2="0.4">
          <stop offset="0" stop-color="var(--band-light)"/>
          <stop offset="0.6" stop-color="#761519"/>
          <stop offset="1" stop-color="var(--band-dark)"/>
        </linearGradient>
      </defs>
      <path d="M0 300 C 250 345, 620 355, 1000 296 L1000 570 L0 570 Z" fill="url(#bandFill)"/>
      <path d="M0 312 C 260 358, 620 366, 1000 306" fill="none" stroke="var(--accent-line)" stroke-width="4"/>
    </svg>

    <div class="brand-mark"></div>
    <div class="brand-name">
      <span class="brand-word">VORNALY</span>
      <span class="brand-rule"></span>
      <span class="brand-tagline">HEALTH CARE MARKETING</span>
    </div>

    <div class="card-holder">
      <div class="holder-name">MARNIE OKONSKI</div>
      <div class="holder-role">CEO</div>
    </div>

    <ul class="contact-list">
      <li class="contact-item">
        <svg class="contact-icon" viewBox="0 0 24 24" aria-hidden="true"><path d="M6.6 10.8a15.1 15.1 0 0 0 6.6 6.6l2.2-2.2a1 1 0 0 1 1-.25 11.4 11.4 0 0 0 3.6.57 1 1 0 0 1 1 1V20a1 1 0 0 1-1 1A17 17 0 0 1 3 4a1 1 0 0 1 1-1h3.5a1 1 0 0 1 1 1c0 1.25.2 2.45.57 3.57a1 1 0 0 1-.25 1z"/></svg>
        (502)638-2947
      </li>
      <li class="contact-item">
        <svg class="contact-icon" viewBox="0 0 24 24" aria-hidden="true"><path d="M2 5h20v14H2z M3.5 6.5 12 13l8.5-6.5" fill-rule="evenodd"/><path d="M2 5l10 8 10-8v2l-10 8L2 7z" fill="#7a1519"/></svg>
        MARNIE@VORNALY.COM
      </li>
      <li class="contact-item">
        <svg class="contact-icon" viewBox="0 0 24 24" aria-hidden="true"><circle cx="12" cy="12" r="10"/><path d="M2 12h20M12 2c3 3 3 17 0 20M12 2c-3 3-3 17 0 20" fill="none" stroke="#7a1519" stroke-width="1.6"/></svg>
        WWW.VORNALY.COM
      </li>
    </ul>
  </div>
</body>
</html>
```